依頼詳細
【サイトの最大の要望】
・ターゲットに合った分かりやすいデザイン

【強み】
・整体と美容の両方からお客様の身体の不調やなりたい自分に合った施術を行える点です。

【おすすめメニュー】
・お客様の身体の不調や気になる部分に合わせたオーダーメイドの施術

【ターゲット】
・30代・40代の会社員、自営、パートなど自分にかけるお金がある人。

【デザインについて】
・部分的に参考サイトのようなフレームを使用していただきたいです。
・参考サイトの「お知らせ」の背景で使用しているような
お花などのボタニカルなイラストなど入れてほしいです。

【参考サイト】
・tonsor HALVEN MOREL(トンソル ハルヴェン モレル)
http://morel-tonsor.example/
白を基調としている点や、上品なゴールドのフォント、「お知らせ」の背景で使用している
お花のイラストをアクセントで使用しているところが気に入っています。

http://quillmere-works.example/
とても見やすくて分かりやすくていいなと思っています。

http://vesna-lumio.example/
フレームや両隅の装飾が好きです。

http://kp-dermaluxe.example/
色合いやテクスチャー、お花のイラストなどが女性らしい雰囲気でイメージに一番近いです。

【サイトマップ】
①TOP
② アクセス
③初めての方へ
④プロフィール
⑤ 当サロンの特徴
⑥身体の外側の不調(痛み・しびれ)
⑦身体の内側の不調(内臓などの不調・冷え症・アトピー)
⑧ストレス
⑨顔に関するお悩み
⑩体に関するお悩み
⑪リラクゼーション
⑫お客様の声
⑬キャンペーン、特典
⑭セミナー・スクールのご案内
⑮料金
⑯ニュース(一覧)
∟⑰ニュース(詳細)
⑱ブログ(一覧)
∟⑲ブログ(詳細)
⑳予約、お問い合わせ、プライバシー・ポリシー

■TOPページにGメニューとは別にデザインの入り口を必須で設けて頂きたいコンテンツは以下となります。
(それ以外のページに関してはランサーにお任せします)

タイトル:メニュー
⑥身体の外側の不調(痛み・しびれ)
⑧ストレス
⑨顔に関するお悩み
⑩体に関するお悩み
⑪リラクゼーション

⑫お客様の声
⑬キャンペーン、特典
⑰ニュース(詳細)
⑲ブログ(詳細)

下記のボタンもしくはバナー希望です。
・予約
・お問い合わせ
・キャンペーン
サイトURL
https://trelvane.sitebloomer.example/
ページ数
1ページ
希望イメージ
シンプル 複雑
単色 カラフル
暗い 明るい
日常 高級
遊び心 厳粛
未来的 伝統的
女性的 男性的
希望する色
緑系、ゴールド
納品ファイル
• イラストレーター形式 (.ai)
• フォトショップ形式 (.psd)
• PNG形式 (.png)
補足説明
【店舗へのご連絡はおやめください】
ワークリンク規約にもありますが、店舗への通常業務に支障が出るため、
直接電話等のお問い合わせをお控え頂きますよう、ご協力願います。

【素材写真】
下記よりダウンロードしてご使用ください。
https://3.filedrift.example/0225-k81937b52c904f6a13bd7e2059c771b3
TOPイメージを添付しましたので、延長を希望いたします。

下記よりダウンロードしてご参照ください。
https://20.filedrift.example/0131-p47390a81be527c09d6f1a38e4b92c05

ご多忙のところ恐縮ですが、宜しくお願いいたします。
テキストや画像などのダミーは無い状態でご提案をお願いいたします。

全体的にバランスが良く、整体っぽくないメインビジュアルが特に良かったです。

たくさんのご提案、ありがとうございました。
どのデザインも素敵で選定が難しかったです。

また、何か機会がありましたら、宜しくお願いいたします。

```html
<!DOCTYPE html>
<html lang="ja">
<head>
<meta charset="utf-8">
<title>Trelvane Works | 美容矯正サロン</title>
<link rel="stylesheet" href="https://fonts.googleapis.com/css2?family=Great+Vibes&family=Noto+Serif+JP:wght@400;500;700&family=Noto+Sans+JP:wght@400;500&display=swap">
<style>
:root{
  --gold:#b08d57;
  --gold-dark:#8e6d3c;
  --gold-light:#d9c39a;
  --green:#5d7d4c;
  --green-dark:#3f5a34;
  --mint:#e9f4ee;
  --ink:#4a4037;
  --muted:#7a7068;
  --line:#e2d6c2;
  --paper:#fffdf9;
  --pink:#e98aa6;
  --leaf:#8fc46b;
  --violet:#a98bd6;
  --amber:#e7a24c;
  --plum:#c07ccb;
}
*{box-sizing:border-box;margin:0;padding:0}
html,body{width:1200px;height:4920px;overflow:hidden}
body{background:#fff;color:var(--ink);font-family:"Noto Serif JP",serif;font-size:15px;line-height:1.8}
.page{position:relative;width:1200px;height:4920px;overflow:hidden}

/* header */
.site-header{height:120px;display:flex;align-items:center;padding:0 36px;gap:20px;background:#fff}
.brand{display:flex;flex-direction:column;line-height:1.15;color:var(--gold-dark);white-space:nowrap;flex:none}
.brand-sub{font-size:13px;letter-spacing:.05em}
.brand-name{font-size:26px;font-weight:500}
.global-nav{display:flex;gap:12px;flex:1;justify-content:center}
.global-nav a{display:flex;flex-direction:column;align-items:center;text-decoration:none;color:var(--gold-dark);font-size:16px;line-height:1.3;white-space:nowrap}
.global-nav small{font-size:9px;color:var(--muted);font-family:"Noto Sans JP",sans-serif}
.header-actions{display:flex;gap:8px;flex:none}
.btn{display:inline-flex;align-items:center;justify-content:center;text-decoration:none;font-family:"Noto Serif JP",serif;white-space:nowrap}
.btn-outline{border:1px solid var(--gold);color:var(--gold-dark);background:#fff}
.btn-fill{background:var(--gold);color:#fff}
.header-actions .btn{height:38px;padding:0 12px;font-size:11px}

.hero{height:520px;background:linear-gradient(120deg,#efe2d8 0%,#c9a995 40%,#7d5d4c 70%,#d9c6d9 100%)}

/* section titles */
.sec-title{text-align:center;color:var(--gold)}
.sec-title .en{font-family:"Great Vibes",cursive;font-size:62px;line-height:1}
.sec-title .ja{font-size:14px;color:var(--gold-dark);letter-spacing:.15em}
.more{display:block;width:220px;height:36px;margin:0 auto;border:1px solid var(--gold-light);background:var(--gold-light);color:#fff;font-size:12px;line-height:36px;text-align:center;text-decoration:none}

.deco{position:absolute}

/* features */
.features{position:relative;height:560px;padding-top:60px;background:#fff}
.features .deco-left{left:0;top:30px;width:230px;height:300px;border-radius:0 50% 50% 0;background:linear-gradient(160deg,#f3dfe6,#dfeadf)}
.features .deco-right{right:0;top:110px;width:210px;height:330px;border-radius:50% 0 0 50%;background:linear-gradient(200deg,#e6dff3,#f4e7ea)}
.features .lead{text-align:center;color:var(--green);font-size:25px;font-weight:500;margin:14px 0 26px}
.features .body{width:540px;margin:0 auto 30px;text-align:center;font-size:15px}

/* flows */
.flows{position:relative;height:440px;background:linear-gradient(180deg,#fff,#f7f3ee 60%,#fff)}
.flows .deco-right{right:0;top:240px;width:210px;height:200px;border-radius:50% 0 0 0;background:linear-gradient(200deg,#e4d9ee,#f3e8e1)}
.flow-box{position:absolute;left:180px;top:20px;width:840px;height:400px;background:#fff;border:2px solid var(--line);border-radius:6px;text-align:center;padding-top:22px}
.flow-box .intro{font-size:23px;color:var(--green);line-height:1.5;font-weight:500}
.flow-box .label{font-size:19px;color:var(--green-dark);margin:4px 0 8px}
.flow-list{display:flex;justify-content:center;gap:34px;list-style:none;height:126px}
.flow-list li{width:100px;height:100px;border-radius:50%;color:#fff;display:flex;flex-direction:column;align-items:center;justify-content:center;font-size:17px;line-height:1.2}
.flow-list li:nth-child(even){margin-top:24px}
.flow-list b{font-size:22px;font-weight:500}
.c1{background:var(--pink)}.c2{background:var(--leaf)}.c3{background:var(--violet)}.c4{background:var(--amber)}.c5{background:var(--plum)}
.flow-box .goal{font-size:21px;color:var(--green);margin:8px 0 14px;font-weight:500}

/* menu */
.menu{position:relative;height:780px;padding-top:20px;background:#fbfaf6}
.menu .deco-right{right:0;top:0;width:190px;height:260px;border-radius:0 0 0 60%;background:linear-gradient(200deg,#ece0f1,#f6ecdf)}
.menu .deco-left{left:0;top:520px;width:160px;height:240px;border-radius:0 60% 0 0;background:linear-gradient(160deg,#e5efe0,#f2e3e8)}
.menu-frame{position:absolute;left:210px;top:20px;width:780px;height:740px;border:2px solid var(--gold-light);background:#fff;padding:30px 40px}
.menu-frame::before{content:"";position:absolute;inset:8px;border:1px solid var(--line);pointer-events:none}
.menu-frame .intro{text-align:center;font-size:13px;margin:16px 0 20px}
.menu-grid{display:grid;grid-template-columns:repeat(3,1fr);gap:14px}
.menu-item{position:relative;height:230px;text-decoration:none}
.menu-photo{height:230px}
.menu-item span{position:absolute;left:12px;right:12px;bottom:18px;background:var(--green);color:#fff;text-align:center;font-size:14px;line-height:1.3;padding:8px 4px;border:1px solid var(--gold-light)}
.menu-item span small{display:block;font-size:10px}
.p1{background:linear-gradient(135deg,#d9c1b1,#8d6f60)}
.p2{background:linear-gradient(135deg,#e8d8cb,#a98f80)}
.p3{background:linear-gradient(135deg,#c8b5a6,#6f5a4d)}
.p4{background:linear-gradient(135deg,#e6d3c8,#b39384)}
.p5{background:linear-gradient(135deg,#d2c0b3,#8a6e60)}
.p6{background:linear-gradient(135deg,#eee0d4,#b8a091)}

/* profile */
.profile{position:relative;height:640px;padding-top:40px;background:#fff}
.profile .deco-right{right:0;top:300px;width:200px;height:300px;border-radius:50% 0 0 50%;background:linear-gradient(200deg,#efe4f2,#f3ece3)}
.profile-wrap{display:flex;gap:60px;width:860px;margin:40px auto 0}
.profile-card{width:240px;text-align:center}
.portrait{width:200px;height:200px;border-radius:50%;margin:20px auto 14px;background:linear-gradient(160deg,#f4e4d6,#d9b9a4)}
.profile-card .name{font-size:24px;color:var(--green-dark)}
.profile-card .name small{display:block;font-size:11px;color:var(--muted)}
.profile-card p{font-size:11px;line-height:1.7;margin-top:8px}
.timeline{flex:1;border-collapse:collapse;font-size:12px}
.timeline th{width:110px;text-align:left;vertical-align:top;font-weight:400;color:var(--gold-dark);padding:8px 0;border-bottom:1px solid var(--line)}
.timeline td{padding:8px 0;border-bottom:1px solid var(--line);line-height:1.6}

/* beginners */
.beginners{position:relative;height:600px;padding-top:30px;background:var(--mint)}
.beginners .deco-left{left:0;top:0;width:220px;height:160px;border-radius:0 0 60% 0;background:linear-gradient(160deg,#dcecdd,#f1e6ec)}
.beginners-wrap{display:flex;gap:40px;width:960px;margin:30px auto 0}
.beginners-text{flex:1;font-size:13px;line-height:1.9}
.beginners-text p+p{margin-top:12px}
.beginners-photos{width:420px;display:grid;grid-template-columns:1fr 1fr;gap:10px}
.beginners-photos div{height:110px}
.b1{background:linear-gradient(135deg,#e8ddd2,#b7a08f)}
.b2{background:linear-gradient(135deg,#d9cabb,#8e7565)}
.b3{background:linear-gradient(135deg,#efe6dc,#c9b3a2)}
.b4{background:linear-gradient(135deg,#e4d2c6,#a58877)}

/* news & blog */
.updates{height:420px;display:flex;gap:80px;padding:40px 120px 0;background:#fff}
.updates section{flex:1}
.updates ul{list-style:none;margin-top:18px}
.updates li{display:flex;gap:24px;font-size:12px;padding:9px 0;border-bottom:1px solid var(--line)}
.updates time{color:var(--gold-dark);width:80px;flex:none}

/* banners */
.banners{height:160px;display:flex;justify-content:center;gap:80px;padding-top:20px}
.banner{width:340px;height:130px;border:2px solid var(--gold-light);display:flex;flex-direction:column;align-items:center;justify-content:center;color:var(--gold);text-decoration:none;background:#fff;position:relative}
.banner::before{content:"";position:absolute;inset:6px;border:1px solid var(--line)}
.banner .en{font-family:"Great Vibes",cursive;font-size:56px;line-height:1}
.banner .ja{font-size:13px;color:var(--gold-dark)}

/* access */
.access{height:420px;padding-top:30px;background:#fff}
.access-wrap{display:flex;align-items:center;justify-content:center;gap:60px;width:860px;margin:24px auto 0}
.access .brand{width:340px;align-items:center}
.access .brand-name{font-size:42px}
.access .brand-sub{font-size:19px}
.info{font-size:12px;border-collapse:collapse}
.info th{font-weight:400;color:var(--gold-dark);text-align:left;padding:3px 16px 3px 0;vertical-align:top;white-space:nowrap}
.info td{padding:3px 0}
.access-actions{display:flex;justify-content:center;gap:40px;margin-top:30px}
.access-actions .btn{width:300px;height:52px;font-size:16px}

/* footer */
.site-footer{height:260px;background:var(--mint);padding:32px 120px 0;position:relative}
.footer-nav{display:flex;gap:70px}
.footer-nav div{font-size:11px;line-height:1.65}
.footer-nav h4{font-weight:500;font-size:12px;color:var(--green-dark)}
.footer-nav ul{list-style:none}
.footer-nav li::before{content:"› ";color:var(--gold)}
.copyright{position:absolute;left:0;right:0;bottom:0;height:30px;line-height:30px;background:var(--green);color:#fff;text-align:center;font-size:11px}
</style>
</head>
<body>
<div class="page">

<header class="site-header">
  <div class="brand"><span class="brand-sub">Hoshizaki 美容矯正サロン</span><span class="brand-name">Trelvane Works</span></div>
  <nav class="global-nav">
    <a href="#">Top<small>トップ</small></a>
    <a href="#">Features<small>当サロンの特徴</small></a>
    <a href="#">Menu<small>メニュー</small></a>
    <a href="#">Beginners<small>初めての方へ</small></a>
    <a href="#">Campaign<small>キャンペーン・特典</small></a>
    <a href="#">Price<small>料金</small></a>
    <a href="#">News<small>ニュース</small></a>
    <a href="#">Blog<small>ブログ</small></a>
    <a href="#">Access<small>アクセス</small></a>
  </nav>
  <div class="header-actions">
    <a class="btn btn-outline" href="#">セミナー・スクールのご案内</a>
    <a class="btn btn-fill" href="#">ご予約・お問い合わせ</a>
  </div>
</header>

<div class="hero" role="img" aria-label="施術者が横になった女性の首元をやさしくほぐすメインビジュアル写真"></div>

<section class="features">
  <div class="deco deco-left" role="img" aria-label="淡い花のボタニカルイラスト"></div>
  <div class="deco deco-right" role="img" aria-label="淡い花のボタニカルイラスト"></div>
  <div class="sec-title"><div class="en">Features</div><div class="ja">当サロンの特徴</div></div>
  <p class="lead">身体のなかが整う だから綺麗になる</p>
  <p class="body">例えば、顔のくすみ<br>それは、血行不良やリンパの流れが滞り、<br>老廃物が蓄積されて起こるのです。<br>お肌の中の巡りを整えることで<br>できにくい身体へと変わっていきます。<br>表面だけではなく内側から<br>本来の美しさを引き出します。</p>
  <a class="more" href="#">詳しくはこちら</a>
</section>

<section class="flows">
  <div class="deco deco-right" role="img" aria-label="淡い花のボタニカルイラスト"></div>
  <div class="flow-box">
    <p class="intro">Trelvane Worksでは、美容矯正と整体で<br>5つの流れが整うように施術を行っています。</p>
    <p class="label">5つの流れとは</p>
    <ol class="flow-list">
      <li class="c1"><b>1</b>血流</li>
      <li class="c2"><b>2</b>リンパ</li>
      <li class="c3"><b>3</b>呼吸</li>
      <li class="c4"><b>4</b>脳脊髄液</li>
      <li class="c5"><b>5</b>筋膜</li>
    </ol>
    <p class="goal">5つの流れを整えて綺麗と健康を両方手に入れよう!</p>
    <a class="more" href="#">詳しくはこちら</a>
  </div>
</section>

<section class="menu">
  <div class="deco deco-right" role="img" aria-label="淡い花のボタニカルイラスト"></div>
  <div class="deco deco-left" role="img" aria-label="淡い花のボタニカルイラスト"></div>
  <div class="menu-frame">
    <div class="sec-title"><div class="en">Menu</div><div class="ja">メニュー</div></div>
    <p class="intro">Trelvane Worksでは、お客様の不調やなりたい姿に合わせて、<br>身体の内と外からオーダーメイドの施術を行っています。<br>気になるお悩みからメニューをお選びください。</p>
    <div class="menu-grid">
      <a class="menu-item" href="#"><div class="menu-photo p1" role="img" aria-label="肩まわりの施術写真"></div><span>身体の外側の不調<small>(痛み・しびれ)</small></span></a>
      <a class="menu-item" href="#"><div class="menu-photo p2" role="img" aria-label="お腹まわりの施術写真"></div><span>身体の内側の不調<small>(内臓などの不調・冷え症・アトピー)</small></span></a>
      <a class="menu-item" href="#"><div class="menu-photo p3" role="img" aria-label="頭部をほぐす施術写真"></div><span>ストレス</span></a>
      <a class="menu-item" href="#"><div class="menu-photo p4" role="img" aria-label="フェイシャル施術写真"></div><span>顔に関するお悩み</span></a>
      <a class="menu-item" href="#"><div class="menu-photo p5" role="img" aria-label="背中の施術写真"></div><span>体に関するお悩み</span></a>
      <a class="menu-item" href="#"><div class="menu-photo p6" role="img" aria-label="リラックスした施術風景写真"></div><span>リラクゼーション</span></a>
    </div>
  </div>
</section>

<section class="profile">
  <div class="deco deco-right" role="img" aria-label="淡い花のボタニカルイラスト"></div>
  <div class="sec-title"><div class="en">Profile</div><div class="ja">プロフィール</div></div>
  <div class="profile-wrap">
    <div class="profile-card">
      <div class="portrait" role="img" aria-label="施術者のプロフィール写真"></div>
      <p class="name">宮下 彩乃<small>Ayano Miyashita</small></p>
      <p>大学卒業後、事務職に就くも体調を崩し、整体・リフレクソロジーの道を歩み始める。</p>
    </div>
    <table class="timeline">
      <tr><th>2003年</th><td>整体師養成スクールにてボディケアの基礎を学ぶ<br>整体院にて勤務、多くのお客様の施術を担当</td></tr>
      <tr><th>2006年</th><td>美容整体を習得</td></tr>
      <tr><th>2008年</th><td>美容矯正サロンにて勤務<br>フェイシャル技術を習得</td></tr>
      <tr><th>2012年5月</th><td>港北みどり市にて美容矯正サロンを開業</td></tr>
      <tr><th>2015年</th><td>美容矯正セミナー講師として活動開始</td></tr>
      <tr><th>同年</th><td>美容整体協会認定講師に就任<br>リフトアップ技術認定 取得</td></tr>
      <tr><th>2018年10月</th><td>スクール部門を開設<br>セミナー・スクールの運営を開始</td></tr>
    </table>
  </div>
</section>

<section class="beginners">
  <div class="deco deco-left" role="img" aria-label="淡い花のボタニカルイラスト"></div>
  <div class="sec-title"><div class="en">Beginners</div><div class="ja">初めての方へ</div></div>
  <div class="beginners-wrap">
    <div class="beginners-text">
      <p>Trelvane Worksは、<br>落ち着いたプライベート空間で、丁寧なカウンセリングから始まります。初めての方もどうぞ安心してご来店ください。</p>
      <p>◆当日の流れ<br>ご予約の時間に合わせてお越しいただき、お身体の状態やお悩みを伺います。その後、お一人おひとりに合わせた施術を行います。</p>
      <p>◆お支払いについて<br>施術後に受付にてお会計をお願いいたします。</p>
      <p>◆ご予約について<br>完全予約制となっております。お電話またはお問い合わせフォームよりご予約ください。ご不明な点はお気軽にご相談ください。</p>
    </div>
    <div class="beginners-photos">
      <div class="b1" role="img" aria-label="カウンセリングの様子の写真"></div>
      <div class="b2" role="img" aria-label="施術中の写真"></div>
      <div class="b3" role="img" aria-label="サロン室内の写真"></div>
      <div class="b4" role="img" aria-label="施術ベッドの写真"></div>
    </div>
  </div>
</section>

<div class="updates">
  <section>
    <div class="sec-title"><div class="en">News</div><div class="ja">ニュース</div></div>
    <ul>
      <li><time>2020.02</time>ホームページをリニューアルしました!</li>
      <li><time>2017.09.28</time>美容矯正の体験会を開催いたします</li>
      <li><time>2017.08.08</time>夏季休業のお知らせ</li>
      <li><time>2017.07.20</time>入門セミナーのご案内</li>
      <li><time>2017.06.07</time>美容矯正スクール開講のお知らせ</li>
      <li><time>2017.04.07</time>新メニュー リフトアップコースがスタートしました!</li>
    </ul>
  </section>
  <section>
    <div class="sec-title"><div class="en">Blog</div><div class="ja">ブログ</div></div>
    <ul>
      <li><time>2018.12.20</time>季節の変わり目の体調管理</li>
      <li><time>2018.12.06</time>冷え性改善のためにできること</li>
      <li><time>2018.11.26</time>お顔のむくみと姿勢の関係</li>
      <li><time>2018.11.21</time>呼吸を整えると変わること</li>
      <li><time>2018.11.15</time>肩こりとストレスのお話</li>
      <li><time>2018.11.03</time>リンパの流れと美肌について</li>
    </ul>
  </section>
</div>

<div class="banners">
  <a class="banner" href="#"><span class="en">Voice</span><span class="ja">お客様の声</span></a>
  <a class="banner" href="#"><span class="en">Campaign</span><span class="ja">キャンペーン・特典</span></a>
</div>

<section class="access">
  <div class="sec-title"><div class="en">Access</div><div class="ja">アクセス</div></div>
  <div class="access-wrap">
    <div class="brand"><span class="brand-sub">Hoshizaki 美容矯正サロン</span><span class="brand-name">Trelvane Works</span></div>
    <table class="info">
      <tr><th>住所</th><td>港北みどり市若葉台2-18-4<br>さくらテラス 2F</td></tr>
      <tr><th>電話番号</th><td>000-123-4567</td></tr>
      <tr><th>営業時間</th><td>月〜金 10:00〜19:00(最終受付)<br>土・日 10:00〜18:00(最終受付)</td></tr>
      <tr><th>定休日</th><td>不定休</td></tr>
    </table>
  </div>
  <div class="access-actions">
    <a class="btn btn-fill" href="#">セミナー・スクールのご案内</a>
    <a class="btn btn-fill" href="#">ご予約・お問い合わせ</a>
  </div>
</section>

<footer class="site-footer">
  <nav class="footer-nav">
    <div><h4>当院のご紹介</h4><ul><li>トップ</li><li>当サロンの特徴</li><li>初めての方へ</li><li>キャンペーン・特典</li><li>料金</li><li>ニュース</li><li>ブログ</li></ul></div>
    <div><h4>メニュー</h4><ul><li>身体の外側の不調(痛み・しびれ)</li><li>身体の内側の不調(内臓などの不調・冷え症・アトピー)</li><li>ストレス</li><li>顔に関するお悩み</li><li>体に関するお悩み</li><li>リラクゼーション</li></ul></div>
    <div><h4>ピックアップ</h4><ul><li>プロフィール</li><li>お客様の声</li><li>セミナー・スクールのご案内</li><li>ご予約・お問い合わせ</li><li>プライバシー・ポリシー</li></ul></div>
  </nav>
  <p class="copyright">Copyright 2020 Trelvane Works All Rights Reserved</p>
</footer>

</div>
</body>
</html>
```